Brand new website for global research and investment startup

We need a simple website, maybe 3 pages: landing page with business description, investment philosophy, team and contact info.
We have a logo already that can be incorporated. Please use the logo only, not the text
We like the color green, something along the lines of #3D6C32 as the main color.
We'd like to design the website with geometric shapes in gradations of the base color. The shapes should suggest "work in progress", "built to last (a long time)", "solidity" and "indestructibility". One idea floating in my head sees smaller features with icosahedron and dodecahedron shapes, and maybe larger structures like crystal lattices; but please feel free to be creative and imagine your own.

```html
<!DOCTYPE html>
<html lang="en">
<head>
<meta charset="utf-8">
<title>Hollis Crest Investment Group – Responsive Layouts</title>
<link rel="stylesheet" href="https://fonts.googleapis.com/css2?family=Inter:wght@400;500;600&family=Roboto+Condensed:wght@500;700&display=swap">
<style>
:root{
  --green:#3d6c32;
  --green-mid:#5a8a4c;
  --green-light:#8db27e;
  --green-dark:#1f3d1c;
  --green-deep:#142a14;
  --ink:#1d261c;
  --text:#3b3f3a;
  --muted:#6b706a;
  --line:#e6ebe4;
  --card-shadow:0 2px 10px rgba(30,50,30,.08);
  --footer:#1c1e1b;
  --footer-text:#c9ccc7;
  --white:#ffffff;
  --canvas:#f4f5f3;
}
*{box-sizing:border-box;margin:0;padding:0}
html,body{width:1200px;height:800px;overflow:hidden;background:var(--canvas)}
body{font-family:"Inter",Arial,sans-serif;color:var(--text)}
.stage{position:absolute;left:0;top:0;width:1536px;height:1024px;transform:scale(.78125);transform-origin:0 0}
.screen{position:absolute;background:var(--white);overflow:hidden;box-shadow:0 3px 14px rgba(0,0,0,.12);border-radius:4px}
.abs{position:absolute}
.brand{font-family:"Roboto Condensed",Arial,sans-serif;font-weight:700;color:var(--green-dark);letter-spacing:.3px}
.h-display{font-family:"Roboto Condensed",Arial,sans-serif;font-weight:700;color:#fff;text-transform:uppercase}
.h-section{font-family:"Roboto Condensed",Arial,sans-serif;font-weight:700;color:var(--green-dark)}
.eyebrow{font-weight:600;color:var(--green);text-transform:uppercase;letter-spacing:.3px}
.btn{position:absolute;display:flex;align-items:center;justify-content:center;background:var(--green);color:#fff;border-radius:999px;font-family:"Roboto Condensed",Arial,sans-serif;font-weight:700;text-transform:uppercase;letter-spacing:.3px;white-space:nowrap}
.nav-link{position:absolute;top:19px;font-size:9.5px;color:var(--ink);white-space:nowrap}
.nav-link.active{color:var(--green-dark);border-bottom:1.5px solid var(--green);padding-bottom:3px}
.hero{position:absolute;left:0;width:100%;background:linear-gradient(100deg,var(--green-deep) 0%,var(--green-dark) 40%,#2d5327 100%)}
.hero-photo{position:absolute;top:0;height:100%;background:linear-gradient(180deg,#c8d6df 0%,#8ea3ad 35%,#5f7b78 65%,#3a5a34 100%);-webkit-mask-image:linear-gradient(90deg,transparent 0,#000 30%);mask-image:linear-gradient(90deg,transparent 0,#000 30%)}
.hero-wave{position:absolute;left:0;bottom:-1px;width:100%}
.hero p{color:#e7eee4}
.crystal{position:absolute;background:radial-gradient(circle at 45% 40%,#8fb57f 0%,#5a8a4c 40%,#2f5a28 75%,rgba(255,255,255,0) 76%)}
.card{position:absolute;background:#fff;border:1px solid var(--line);border-radius:6px;box-shadow:var(--card-shadow)}
.card h3{font-family:"Roboto Condensed",Arial,sans-serif;font-weight:700;color:var(--green-dark)}
.card p{color:var(--text)}
.step{position:absolute;text-align:center}
.step h4{font-family:"Roboto Condensed",Arial,sans-serif;font-weight:700;color:var(--ink)}
.step p{color:var(--text)}
.dots{position:absolute;border-top:2px dotted var(--green-mid)}
.dots::after{content:"";position:absolute;right:-3px;top:-4px;width:5px;height:5px;border-radius:50%;background:var(--green-mid)}
.portrait{position:absolute;background:linear-gradient(180deg,#b9bcb8 0%,#8e918d 55%,#3b3f44 100%);border-radius:3px}
.portrait.round{border-radius:50%}
.member{position:absolute;text-align:center}
.member .name{color:var(--ink)}
.member .role{color:var(--muted)}
.footer{position:absolute;left:0;width:100%;background:var(--footer);color:var(--footer-text)}
.footer h5{color:#fff;font-weight:500}
.footer ul{list-style:none}
.social{display:flex}
.social span{display:block;border:1.5px solid #fff;border-radius:50%}
.social.filled span{background:var(--green);border:none}
.copyright{position:absolute;left:0;width:100%;text-align:center;color:#c3c6c1}
.burger{position:absolute;width:19px;height:14px;border-top:2px solid var(--ink);border-bottom:2px solid var(--ink)}
.burger::after{content:"";position:absolute;left:0;right:0;top:4px;border-top:2px solid var(--ink)}
.ico{position:absolute;color:var(--green)}
</style>
</head>
<body>
<svg width="0" height="0" style="position:absolute">
  <defs>
    <symbol id="i-shield" viewBox="0 0 24 24"><path d="M12 2 4 5v6c0 5 3.4 9.3 8 11 4.6-1.7 8-6 8-11V5z" fill="currentColor"/><path d="M12 6 7.5 7.7v3.6c0 3 2 5.6 4.5 6.6 2.5-1 4.5-3.6 4.5-6.6V7.7z" fill="#fff"/></symbol>
    <symbol id="i-shield-line" viewBox="0 0 24 24"><path d="M12 2 4 5v6c0 5 3.4 9.3 8 11 4.6-1.7 8-6 8-11V5z" fill="none" stroke="currentColor" stroke-width="1.6"/><path d="M12 6 7.5 7.7v3.6c0 3 2 5.6 4.5 6.6 2.5-1 4.5-3.6 4.5-6.6V7.7z" fill="none" stroke="currentColor" stroke-width="1.4"/></symbol>
    <symbol id="i-chart" viewBox="0 0 24 24"><rect x="3" y="14" width="3" height="7" fill="currentColor"/><rect x="8" y="11" width="3" height="10" fill="currentColor"/><rect x="13" y="8" width="3" height="13" fill="currentColor"/><rect x="18" y="5" width="3" height="16" fill="currentColor"/><path d="M3 11 9 6l4 3 7-6" fill="none" stroke="currentColor" stroke-width="1.6"/><path d="M17 3h3v3" fill="none" stroke="currentColor" stroke-width="1.6"/></symbol>
    <symbol id="i-people" viewBox="0 0 28 24"><circle cx="8" cy="7" r="3.2" fill="currentColor"/><circle cx="20" cy="7" r="3.2" fill="currentColor"/><circle cx="14" cy="9" r="3.8" fill="currentColor"/><path d="M2 19c0-4 3-6 6-6s4 1 4 1H2zM26 19c0-4-3-6-6-6s-4 1-4 1h10z" fill="currentColor"/><path d="M6 22c0-5 3.6-8 8-8s8 3 8 8z" fill="currentColor"/></symbol>
    <symbol id="i-people-line" viewBox="0 0 28 24"><circle cx="10" cy="7" r="4" fill="none" stroke="currentColor" stroke-width="1.5"/><circle cx="19" cy="8" r="3.4" fill="none" stroke="currentColor" stroke-width="1.5"/><path d="M3 21c0-5 3-8 7-8s7 3 7 8zM18 14c4 0 7 2.5 7 7h-6" fill="none" stroke="currentColor" stroke-width="1.5"/></symbol>
    <symbol id="i-geo" viewBox="0 0 24 24"><g fill="none" stroke="currentColor" stroke-width="1.1" stroke-linejoin="round"><path d="M12 2 20.7 7v10L12 22 3.3 17V7z"/><path d="M12 7 16.5 9.6v5L12 17l-4.5-2.4v-5z"/><path d="M12 2v5M20.7 7l-4.2 2.6M20.7 17l-4.2-2.4M12 22v-5M3.3 17l4.2-2.4M3.3 7l4.2 2.6M12 7 7.5 14.6M12 7l4.5 7.6M7.5 9.6h9"/></g></symbol>
  </defs>
</svg>

<div class="stage">

  <!-- Desktop -->
  <section class="screen desktop" style="left:15px;top:10px;width:797px;height:1005px">
    <header>
      <div class="brand abs" style="left:24px;top:14px;font-size:20px">Hollis Crest</div>
      <nav>
        <span class="nav-link active" style="left:395px">Business Description</span>
        <span class="nav-link" style="left:518px">Investment Philosophy</span>
        <span class="nav-link" style="left:649px">Team</span>
      </nav>
      <div class="btn" style="left:696px;top:12px;width:80px;height:25px;font-size:10.5px;font-family:Inter,Arial,sans-serif;font-weight:500;text-transform:none;letter-spacing:0">Contact Info</div>
    </header>

    <div class="hero" style="top:51px;height:252px">
      <div class="hero-photo" role="img" aria-label="Glass office building against a cloudy sky with green wireframe polyhedra" style="left:360px;width:437px"></div>
      <h1 class="h-display abs" style="left:81px;top:38px;font-size:31px;line-height:35px">Building Enduring<br>Value. Together.</h1>
      <p class="abs" style="left:81px;top:113px;width:245px;font-size:11.5px;line-height:16.5px">We partner with exceptional businesses and management teams to build companies that create long-term, sustainable value.</p>
      <div class="btn" style="left:81px;top:175px;width:113px;height:29px;font-size:11px">Contact Now</div>
      <svg class="hero-wave" viewBox="0 0 797 60" height="60" preserveAspectRatio="none"><path d="M0 48C180 22 330 36 470 40 620 44 720 22 797 0V60H0z" fill="#fff"/></svg>
    </div>

    <div class="crystal" role="img" aria-label="Cluster of green faceted icosahedra linked by a wireframe lattice" style="left:545px;top:305px;width:200px;height:125px;border-radius:50%"></div>

    <div class="eyebrow abs" style="left:42px;top:323px;font-size:8px">Business Description</div>
    <h2 class="h-section abs" style="left:42px;top:336px;font-size:24px">Driving Growth. Creating Value.</h2>
    <p class="abs" style="left:42px;top:366px;width:465px;font-size:9.5px;line-height:14px">Hollis Crest Investment Group partners with high-quality businesses and visionary management teams to accelerate growth and deliver long-term value. We provide strategic guidance, operational expertise, and patient capital to help companies scale, innovate, and lead in their industries.</p>

    <article class="card" style="left:35px;top:428px;width:162px;height:154px;text-align:center">
      <svg class="ico" style="left:63px;top:14px;width:34px;height:34px"><use href="#i-shield"/></svg>
      <h3 style="margin-top:58px;font-size:12.5px">Strong Foundations</h3>
      <p style="font-size:8.3px;line-height:13.5px;margin:8px 20px 0">We invest in businesses with proven models, strong cash flows, and resilient competitive advantages.</p>
    </article>
    <article class="card" style="left:215px;top:428px;width:162px;height:154px;text-align:center">
      <svg class="ico" style="left:59px;top:16px;width:30px;height:30px"><use href="#i-chart"/></svg>
      <h3 style="margin-top:58px;font-size:12.5px;text-align:left;padding-left:26px">Long-Term Focus</h3>
      <p style="font-size:8.3px;line-height:13.5px;margin:8px 30px 0 26px;text-align:left">Our investment horizon is built for the long run, empowering sustainable growth and compounding value.</p>
    </article>
    <article class="card" style="left:395px;top:428px;width:162px;height:154px">
      <svg class="ico" style="left:60px;top:16px;width:36px;height:30px"><use href="#i-people"/></svg>
      <h3 style="margin-top:58px;font-size:12.5px;padding-left:24px">Operational Excellence</h3>
      <p style="font-size:8.3px;line-height:13.5px;margin:8px 20px 0 24px">We work side-by-side with management teams to unlock potential and drive operational improvements.</p>
    </article>
    <article class="card" style="left:581px;top:428px;width:175px;height:154px">
      <svg class="ico" style="left:66px;top:14px;width:34px;height:34px"><use href="#i-geo"/></svg>
      <h3 style="margin-top:58px;font-size:12.5px;padding-left:32px">Built to Last</h3>
      <p style="font-size:8.3px;line-height:13.5px;margin:8px 30px 0 32px">We build companies that are durable, adaptable, and designed to thrive through market cycles.</p>
    </article>

    <h2 class="h-section abs" style="left:51px;top:594px;font-size:20px">Our Core Approach</h2>
    <div class="step" style="left:35px;top:622px;width:110px">
      <svg style="width:34px;height:34px;color:var(--green)"><use href="#i-geo"/></svg>
      <h4 style="font-size:10px;margin-top:6px">Identify</h4>
      <p style="font-size:7.8px;line-height:12px;margin-top:2px">We identify businesses with high potential and strong fundamentals.</p>
    </div>
    <div class="dots" style="left:121px;top:644px;width:70px"></div>
    <div class="step" style="left:185px;top:622px;width:110px">
      <svg style="width:34px;height:34px;color:var(--green)"><use href="#i-geo"/></svg>
      <h4 style="font-size:10px;margin-top:6px">Partner</h4>
      <p style="font-size:7.8px;line-height:12px;margin-top:2px">We partner with management teams to create shared value.</p>
    </div>
    <div class="dots" style="left:272px;top:644px;width:70px"></div>
    <div class="step" style="left:332px;top:622px;width:110px">
      <svg style="width:34px;height:34px;color:var(--green)"><use href="#i-geo"/></svg>
      <h4 style="font-size:10px;margin-top:6px">Build</h4>
      <p style="font-size:7.8px;line-height:12px;margin-top:2px">We build scalable platforms with robust processes and systems.</p>
    </div>
    <div class="dots" style="left:428px;top:644px;width:70px"></div>
    <div class="step" style="left:487px;top:622px;width:110px">
      <svg style="width:34px;height:34px;color:var(--green)"><use href="#i-geo"/></svg>
      <h4 style="font-size:10px;margin-top:6px">Grow</h4>
      <p style="font-size:7.8px;line-height:12px;margin-top:2px">We drive growth through innovation, strategic initiatives, and capital.</p>
    </div>
    <div class="dots" style="left:586px;top:644px;width:70px"></div>
    <div class="step" style="left:643px;top:622px;width:110px">
      <svg style="width:34px;height:34px;color:var(--green)"><use href="#i-geo"/></svg>
      <h4 style="font-size:10px;margin-top:6px">Endure</h4>
      <p style="font-size:7.8px;line-height:12px;margin-top:2px">We create lasting enterprises that stand the test of time.</p>
    </div>

    <div class="abs" style="left:42px;top:728px;width:715px;border-top:1px solid var(--line)"></div>

    <h2 class="h-section abs" style="left:42px;top:748px;font-size:20px">Our Team</h2>
    <p class="abs" style="left:42px;top:780px;width:205px;font-size:8.3px;line-height:13.5px">Our team brings together deep industry experience, investment expertise, and a shared commitment to building enduring value.</p>
    <div class="btn" style="left:43px;top:831px;width:87px;height:21px;font-size:8px">Meet Our Team</div>

    <div class="portrait" role="img" aria-label="Portrait of Daniel Reeve, Managing Partner" style="left:273px;top:742px;width:102px;height:86px"></div>
    <div class="member" style="left:263px;top:836px;width:122px"><div class="name" style="font-size:8.5px">Daniel Reeve</div><div class="role" style="font-size:7px;margin-top:3px">Managing Partner</div></div>
    <div class="portrait" role="img" aria-label="Portrait of Laura Whitfield, Partner" style="left:393px;top:742px;width:102px;height:86px"></div>
    <div class="member" style="left:383px;top:836px;width:122px"><div class="name" style="font-size:8.5px">Laura Whitfield</div><div class="role" style="font-size:7px;margin-top:3px">Partner</div></div>
    <div class="portrait" role="img" aria-label="Portrait of Ethan Cole, Partner" style="left:513px;top:742px;width:102px;height:86px"></div>
    <div class="member" style="left:503px;top:836px;width:122px"><div class="name" style="font-size:8.5px">Ethan Cole</div><div class="role" style="font-size:7px;margin-top:3px">Partner</div></div>
    <div class="portrait" role="img" aria-label="Portrait of Mei Lang, Vice President" style="left:633px;top:742px;width:102px;height:86px"></div>
    <div class="member" style="left:623px;top:836px;width:122px"><div class="name" style="font-size:8.5px">Mei Lang</div><div class="role" style="font-size:7px;margin-top:3px">Vice President</div></div>

    <footer class="footer" style="top:870px;height:135px">
      <div class="brand abs" style="left:42px;top:22px;font-size:18px;color:#fff">Hollis Crest</div>
      <p class="abs" style="left:42px;top:64px;font-size:8.3px;line-height:13.5px">Building exceptional companies.<br>Creating lasting value.</p>
      <div class="abs" style="left:236px;top:18px">
        <h5 style="font-size:10.5px">Quick Links</h5>
        <ul style="font-size:7.8px;line-height:15px;margin-top:6px"><li>Business Description</li><li>Investment Philosophy</li><li>Team</li><li>Contact Info</li></ul>
      </div>
      <div class="abs" style="left:365px;top:18px">
        <h5 style="font-size:10.5px">Resources</h5>
        <ul style="font-size:7.8px;line-height:15px;margin-top:6px"><li>Portfolio</li><li>News &amp; Insights</li><li>Careers</li><li>Privacy Policy</li></ul>
      </div>
      <div class="abs" style="left:486px;top:18px">
        <h5 style="font-size:10.5px">Contact</h5>
        <ul style="font-size:7.2px;line-height:12.5px;margin-top:6px;padding-left:18px;position:relative">
          <li style="position:relative"><svg style="position:absolute;left:-18px;top:2px;width:9px;height:10px" viewBox="0 0 12 14"><path d="M6 1a4.2 4.2 0 0 0-4.2 4.2C1.8 8.4 6 13 6 13s4.2-4.6 4.2-7.8A4.2 4.2 0 0 0 6 1z" fill="none" stroke="#fff" stroke-width="1.3"/><circle cx="6" cy="5.2" r="1.4" fill="#fff"/></svg>48 Harbor Lane, Suite 210<br>Riverton, NY 10000, USA</li>
          <li style="position:relative;margin-top:2px"><svg style="position:absolute;left:-18px;top:3px;width:10px;height:8px" viewBox="0 0 12 9"><rect x=".7" y=".7" width="10.6" height="7.6" fill="none" stroke="#fff" stroke-width="1.2"/><path d="M1 1l5 4 5-4" fill="none" stroke="#fff" stroke-width="1.2"/></svg>info@holliscrest.example</li>
          <li style="position:relative;margin-top:2px"><svg style="position:absolute;left:-18px;top:2px;width:10px;height:10px" viewBox="0 0 12 12"><path d="M2.5 1 4.5 1 5.5 3.8 4.2 5a7 7 0 0 0 2.8 2.8l1.2-1.3 2.8 1v2A1.5 1.5 0 0 1 9.5 11 9 9 0 0 1 1 2.5 1.5 1.5 0 0 1 2.5 1z" fill="none" stroke="#fff" stroke-width="1.1"/></svg>+1 (555) 014-2277</li>
        </ul>
      </div>
      <div class="abs" style="left:657px;top:40px">
        <h5 style="font-size:10.5px">Follow Us</h5>
        <div class="social" style="gap:8px;margin-top:10px"><span style="width:18px;height:18px"></span><span style="width:18px;height:18px"></span><span style="width:18px;height:18px"></span><span style="width:18px;height:18px"></span></div>
      </div>
      <div class="abs" style="left:0;top:104px;width:100%;border-top:1px solid #2f322e"></div>
      <div class="copyright" style="top:116px;font-size:8.3px">© 2025 Hollis Crest Investment Group. All rights reserved.</div>
    </footer>
  </section>

  <!-- Tablet -->
  <section class="screen tablet" style="left:833px;top:10px;width:432px;height:1005px">
    <div class="brand abs" style="left:20px;top:14px;font-size:18px">Hollis Crest</div>
    <div class="burger" style="left:391px;top:18px"></div>

    <div class="hero" style="top:50px;height:232px">
      <div class="hero-photo" role="img" aria-label="Glass office building against a cloudy sky with green wireframe polyhedra" style="left:170px;width:262px"></div>
      <h1 class="h-display abs" style="left:21px;top:23px;font-size:21px;line-height:26px">Building Enduring<br>Value. Together.</h1>
      <p class="abs" style="left:21px;top:83px;width:190px;font-size:8.5px;line-height:13.5px">We partner with exceptional businesses and management teams to build companies that create long-term, sustainable value.</p>
      <div class="btn" style="left:21px;top:137px;width:97px;height:25px;font-size:9px">Contact Now</div>
      <svg class="hero-wave" viewBox="0 0 432 50" height="50" preserveAspectRatio="none"><path d="M0 42C110 18 220 34 300 30 360 27 410 22 432 32V50H0z" fill="#fff"/></svg>
    </div>

    <div class="crystal" role="img" aria-label="Cluster of green faceted icosahedra linked by a wireframe lattice" style="left:285px;top:265px;width:130px;height:105px;border-radius:50%"></div>

    <div class="eyebrow abs" style="left:18px;top:279px;font-size:7.5px">Business Description</div>
    <h2 class="h-section abs" style="left:18px;top:292px;font-size:16px">Driving Growth. Creating Value.</h2>
    <p class="abs" style="left:18px;top:317px;width:250px;font-size:7.5px;line-height:13px">Hollis Crest Investment Group partners with high-quality businesses and visionary management teams to accelerate growth and deliver long-term value.</p>

    <article class="card" style="left:16px;top:372px;width:175px;height:90px">
      <svg class="ico" style="left:16px;top:20px;width:24px;height:24px"><use href="#i-shield-line"/></svg>
      <h3 style="position:absolute;left:51px;top:13px;font-size:8.5px">Strong Foundations</h3>
      <p style="position:absolute;left:51px;top:26px;width:110px;font-size:6.6px;line-height:11.2px">We invest in businesses with proven models, strong cash flows, and resilient competitive advantages.</p>
    </article>
    <article class="card" style="left:207px;top:372px;width:202px;height:90px">
      <svg class="ico" style="left:16px;top:22px;width:22px;height:22px"><use href="#i-chart"/></svg>
      <h3 style="position:absolute;left:54px;top:13px;font-size:8.5px">Long-Term Focus</h3>
      <p style="position:absolute;left:54px;top:26px;width:110px;font-size:6.6px;line-height:11.2px">Our investment horizon is built for the long run, empowering sustainable growth and compounding value.</p>
    </article>
    <article class="card" style="left:16px;top:472px;width:175px;height:86px">
      <svg class="ico" style="left:14px;top:16px;width:28px;height:24px"><use href="#i-people-line"/></svg>
      <h3 style="position:absolute;left:51px;top:14px;font-size:8.5px">Operational Excellence</h3>
      <p style="position:absolute;left:51px;top:27px;width:110px;font-size:6.6px;line-height:11.2px">We work side-by-side with management teams to unlock potential and drive operational improvements.</p>
    </article>
    <article class="card" style="left:207px;top:472px;width:202px;height:86px">
      <svg class="ico" style="left:14px;top:16px;width:28px;height:28px"><use href="#i-geo"/></svg>
      <h3 style="position:absolute;left:54px;top:14px;font-size:8.5px">Built to Last</h3>
      <p style="position:absolute;left:54px;top:27px;width:110px;font-size:6.6px;line-height:11.2px">We build companies that are durable, adaptable, and designed to thrive through market cycles.</p>
    </article>

    <h2 class="h-section abs" style="left:0;top:576px;width:100%;text-align:center;font-size:14.5px">Our Core Approach</h2>
    <div class="step" style="left:16px;top:604px;width:60px"><svg style="width:30px;height:30px;color:var(--green)"><use href="#i-geo"/></svg><h4 style="font-size:8px;margin-top:5px">Identify</h4></div>
    <div class="dots" style="left:76px;top:620px;width:14px"></div>
    <div class="step" style="left:95px;top:604px;width:60px"><svg style="width:30px;height:30px;color:var(--green)"><use href="#i-geo"/></svg><h4 style="font-size:8px;margin-top:5px">Partner</h4></div>
    <div class="dots" style="left:156px;top:620px;width:14px"></div>
    <div class="step" style="left:175px;top:604px;width:60px"><svg style="width:30px;height:30px;color:var(--green)"><use href="#i-geo"/></svg><h4 style="font-size:8px;margin-top:5px">Build</h4></div>
    <div class="dots" style="left:238px;top:620px;width:14px"></div>
    <div class="step" style="left:259px;top:604px;width:60px"><svg style="width:30px;height:30px;color:var(--green)"><use href="#i-geo"/></svg><h4 style="font-size:8px;margin-top:5px">Grow</h4></div>
    <div class="dots" style="left:321px;top:620px;width:14px"></div>
    <div class="step" style="left:347px;top:604px;width:60px"><svg style="width:30px;height:30px;color:var(--green)"><use href="#i-geo"/></svg><h4 style="font-size:8px;margin-top:5px">Endure</h4></div>

    <div class="abs" style="left:0;top:676px;width:100%;border-top:1px solid var(--line)"></div>
    <h2 class="h-section abs" style="left:18px;top:683px;font-size:14.5px">Our Team</h2>
    <div class="portrait" role="img" aria-label="Portrait of Daniel Reeve, Managing Partner" style="left:16px;top:711px;width:81px;height:74px"></div>
    <div class="member" style="left:6px;top:791px;width:101px"><div class="name" style="font-size:7.2px">Daniel Reeve</div><div class="role" style="font-size:6px;margin-top:3px">Managing Partner</div></div>
    <div class="portrait" role="img" aria-label="Portrait of Laura Whitfield, Partner" style="left:111px;top:711px;width:81px;height:74px"></div>
    <div class="member" style="left:101px;top:791px;width:101px"><div class="name" style="font-size:7.2px">Laura Whitfield</div><div class="role" style="font-size:6px;margin-top:3px">Partner</div></div>
    <div class="portrait" role="img" aria-label="Portrait of Ethan Cole, Partner" style="left:207px;top:711px;width:81px;height:74px"></div>
    <div class="member" style="left:197px;top:791px;width:101px"><div class="name" style="font-size:7.2px">Ethan Cole</div><div class="role" style="font-size:6px;margin-top:3px">Partner</div></div>
    <div class="portrait" role="img" aria-label="Portrait of Mei Lang, Vice President" style="left:301px;top:711px;width:81px;height:74px"></div>
    <div class="member" style="left:291px;top:791px;width:101px"><div class="name" style="font-size:7.2px">Mei Lang</div><div class="role" style="font-size:6px;margin-top:3px">Vice President</div></div>
    <div class="btn" style="left:146px;top:819px;width:107px;height:19px;font-size:7px">Meet Our Team</div>

    <footer class="footer" style="top:853px;height:152px">
      <div class="brand abs" style="left:18px;top:26px;font-size:16px;color:#fff">Hollis Crest</div>
      <div class="abs" style="left:166px;top:23px">
        <h5 style="font-size:10px">Quick Links</h5>
        <ul style="font-size:7px;line-height:18px;margin-top:4px"><li>Business Description</li><li>Investment Philosophy</li><li>Team</li><li>Contact Info</li></ul>
      </div>
      <div class="abs" style="left:303px;top:23px">
        <h5 style="font-size:10px">Follow Us</h5>
        <div class="social" style="gap:8px;margin-top:10px"><span style="width:18px;height:18px"></span><span style="width:18px;height:18px"></span><span style="width:18px;height:18px"></span><span style="width:18px;height:18px"></span></div>
      </div>
      <div class="abs" style="left:0;top:130px;width:100%;border-top:1px solid #2f322e"></div>
      <div class="copyright" style="top:141px;font-size:7px">© 2025 Hollis Crest Investment Group. All rights reserved.</div>
    </footer>
  </section>

  <!-- Mobile -->
  <section class="screen mobile" style="left:1285px;top:10px;width:234px;height:1005px">
    <div class="brand abs" style="left:15px;top:14px;font-size:15px">Hollis Crest</div>
    <div class="burger" style="left:199px;top:18px"></div>

    <div class="hero" style="top:48px;height:218px">
      <div class="hero-photo" role="img" aria-label="Glass office building against a cloudy sky" style="left:90px;width:144px"></div>
      <h1 class="h-display abs" style="left:16px;top:22px;font-size:16.5px;line-height:22px">Building Enduring<br>Value. Together.</h1>
      <p class="abs" style="left:16px;top:70px;width:150px;font-size:7.4px;line-height:13.5px">We partner with exceptional businesses and management teams to build companies that create long-term, sustainable value.</p>
      <div class="btn" style="left:16px;top:138px;width:97px;height:25px;font-size:8.5px">Contact Now</div>
      <svg class="hero-wave" viewBox="0 0 234 40" height="40" preserveAspectRatio="none"><path d="M0 34C60 14 130 24 180 18 205 15 222 12 234 16V40H0z" fill="#fff"/></svg>
    </div>

    <div class="crystal" role="img" aria-label="Green faceted icosahedron cluster with wireframe lattice" style="left:142px;top:295px;width:90px;height:82px;border-radius:50%"></div>

    <div class="eyebrow abs" style="left:14px;top:284px;font-size:7px">Business Description</div>
    <h2 class="h-section abs" style="left:14px;top:296px;width:130px;font-size:15px;line-height:20px">Driving Growth. Creating Value.</h2>
    <p class="abs" style="left:14px;top:341px;width:130px;font-size:6.6px;line-height:13px">Hollis Crest Investment Group partners with high-quality businesses and visionary management teams to accelerate growth and deliver long-term value.</p>

    <div class="card" style="left:10px;top:426px;width:101px;height:62px"><svg class="ico" style="left:37px;top:16px;width:28px;height:28px"><use href="#i-shield"/></svg></div>
    <div class="card" style="left:118px;top:426px;width:101px;height:62px"><svg class="ico" style="left:37px;top:17px;width:26px;height:26px"><use href="#i-chart"/></svg></div>
    <div class="card" style="left:10px;top:494px;width:101px;height:62px"><svg class="ico" style="left:34px;top:16px;width:34px;height:28px"><use href="#i-people"/></svg></div>
    <div class="card" style="left:118px;top:494px;width:101px;height:62px"><svg class="ico" style="left:36px;top:14px;width:32px;height:32px"><use href="#i-geo"/></svg></div>

    <h2 class="h-section abs" style="left:0;top:584px;width:100%;text-align:center;font-size:14px">Our Core Approach</h2>
    <div class="step" style="left:1px;top:618px;width:44px"><svg style="width:24px;height:24px;color:var(--green)"><use href="#i-geo"/></svg><h4 style="font-size:7.5px;margin-top:4px">Identify</h4></div>
    <div class="step" style="left:48px;top:618px;width:44px"><svg style="width:24px;height:24px;color:var(--green)"><use href="#i-geo"/></svg><h4 style="font-size:7.5px;margin-top:4px">Partner</h4></div>
    <div class="step" style="left:95px;top:618px;width:44px"><svg style="width:24px;height:24px;color:var(--green)"><use href="#i-geo"/></svg><h4 style="font-size:7.5px;margin-top:4px">Build</h4></div>
    <div class="step" style="left:139px;top:618px;width:44px"><svg style="width:24px;height:24px;color:var(--green)"><use href="#i-geo"/></svg><h4 style="font-size:7.5px;margin-top:4px">Grow</h4></div>
    <div class="step" style="left:186px;top:618px;width:44px"><svg style="width:24px;height:24px;color:var(--green)"><use href="#i-geo"/></svg><h4 style="font-size:7.5px;margin-top:4px">Endure</h4></div>

    <h2 class="h-section abs" style="left:0;top:692px;width:100%;text-align:center;font-size:14px">Our Team</h2>
    <div class="portrait round" role="img" aria-label="Portrait of Daniel Reeve" style="left:8px;top:717px;width:48px;height:48px"></div>
    <div class="portrait round" role="img" aria-label="Portrait of Laura Whitfield" style="left:62px;top:717px;width:48px;height:48px"></div>
    <div class="portrait round" role="img" aria-label="Portrait of Ethan Cole" style="left:117px;top:717px;width:48px;height:48px"></div>
    <div class="portrait round" role="img" aria-label="Portrait of Mei Lang" style="left:174px;top:717px;width:48px;height:48px"></div>
    <div class="btn" style="left:49px;top:785px;width:125px;height:21px;font-size:7.5px">Meet Our Team</div>

    <footer class="footer" style="top:827px;height:178px">
      <div class="brand abs" style="left:15px;top:26px;font-size:14px;color:#fff">Hollis Crest</div>
      <div class="abs" style="left:148px;top:24px">
        <h5 style="font-size:10px">Follow Us</h5>
        <div class="social filled" style="gap:8px;margin-top:10px;margin-left:-13px"><span style="width:14px;height:14px"></span><span style="width:14px;height:14px"></span><span style="width:14px;height:14px"></span><span style="width:14px;height:14px"></span></div>
      </div>
      <div class="copyright" style="top:84px;font-size:7.5px;line-height:14px;padding:0 40px">© 2025 Hollis Crest Investment Group. All rights reserved.</div>
    </footer>
  </section>

</div>
</body>
</html>
```